Harriet Voss Consortium - Paediatric Lower Limb Surgery Agenda Forming Collective

A 2-sided A4 leaflet to explain the research priorities in Children's Orthopaedic Surgery.
We would like this to be similar to that produced previously by the physiotherapists.

```html
<!DOCTYPE html>
<html lang="en">
<head>
<meta charset="utf-8">
<title>Harriet Voss Consortium – Research Priorities Leaflet</title>
<link rel="stylesheet" href="https://fonts.googleapis.com/css2?family=Lato:wght@400;700;900&display=swap">
<style>
:root{
  --backdrop:#6f7d7e;
  --paper:#ffffff;
  --orange:#e8612c;
  --blue:#1f55a6;
  --navy:#15376e;
  --teal:#16868a;
  --crimson:#c0243c;
  --sage:#a9c3a8;
  --periwinkle:#4a6db0;
  --lime:#c9cc3a;
  --maroon:#8c1d33;
  --ink:#111111;
  --cream:#fde9d9;
}
*{box-sizing:border-box;margin:0;padding:0}
html,body{width:1200px;height:3237px;overflow:hidden}
body{background:var(--backdrop);font-family:"Lato",Arial,sans-serif;position:relative;color:var(--ink)}
.sheet{position:absolute;left:65px;width:1070px;background:var(--paper);overflow:hidden;box-shadow:0 4px 14px rgba(0,0,0,.25)}
.sheet--front{top:39px;height:1515px}
.sheet--back{top:1636px;height:1519px}
.front-art{position:absolute;inset:0}
.title{position:absolute;left:54px;top:40px;font-weight:900;font-size:46px;line-height:1.1;color:var(--navy);width:640px}
.subtitle{position:absolute;left:54px;top:165px;font-size:34px;line-height:1.25;color:var(--cream);width:640px;font-weight:400}
.brand-box{position:absolute;left:669px;top:43px;width:401px;height:220px;background:var(--paper);border-radius:14px 0 0 14px;display:flex;align-items:center;gap:18px;padding:0 28px}
.brand-box .dot{width:86px;height:86px;border-radius:50%;background:var(--maroon);flex:none}
.brand-box .name{font-size:40px;line-height:1.1;color:var(--maroon);font-weight:400}
.divider{position:absolute;left:54px;top:320px;width:960px;border-top:2px dotted var(--cream)}
.intro{position:absolute;top:343px;font-size:21px;line-height:1.3;color:#fff;width:400px}
.intro--left{left:54px}
.intro--right{left:550px;width:430px}
.stage{position:absolute;color:#fff}
.stage .label{font-size:29px;font-weight:700}
.stage .word{font-size:46px;font-weight:900;letter-spacing:1px;line-height:1.15}
.stage p{font-size:21px;line-height:1.3;margin-top:12px}
.stage--ask{left:54px;top:880px;width:480px}
.stage--ask .quote{font-weight:700;margin-top:26px}
.stage--analyse{left:727px;top:833px;width:300px}
.stage--analyse .word{color:var(--navy)}
.stage--prioritise{left:118px;top:1364px;color:var(--ink)}
.stage--prioritise .word{color:var(--ink)}
.stage3-text{position:absolute;left:427px;top:1352px;width:610px;font-size:21px;line-height:1.3;color:var(--ink)}
.stage3-text strong{font-weight:900}

.heading{position:absolute;top:38px;left:69px;display:flex;align-items:center}
.heading .lead{font-size:48px;font-weight:900;color:var(--teal);margin-right:22px}
.heading .band{background:var(--orange);color:#fff;font-size:46px;font-weight:900;padding:6px 28px;width:658px;letter-spacing:1px}
.priorities{position:absolute;left:69px;top:129px;width:941px;list-style:none}
.priority{position:relative;height:96px;margin-bottom:20.5px;overflow:hidden;display:flex;align-items:center;color:#fff;font-size:19.5px;line-height:1.3}
.priority .num{position:absolute;top:-22px;width:190px;height:150px;border-radius:50%;background:var(--paper);display:flex;align-items:center;font-size:68px;font-weight:900}
.priority--l .num{left:-70px;justify-content:flex-end;padding-right:40px}
.priority--r .num{right:-70px;justify-content:flex-start;padding-left:36px}
.priority--l .q{margin-left:215px;margin-right:40px}
.priority--r .q{margin-left:30px;margin-right:180px}
.c-orange{background:var(--orange)} .c-orange .num{color:var(--orange)}
.c-teal{background:var(--teal)} .c-teal .num{color:var(--teal)}
.c-crimson{background:var(--crimson)} .c-crimson .num{color:var(--crimson)}
.c-sage{background:var(--sage)} .c-sage .num{color:var(--sage)}
.c-blue{background:var(--periwinkle)} .c-blue .num{color:var(--periwinkle)}
.c-lime{background:var(--lime)} .c-lime .num{color:var(--lime)}
.thanks-note{position:absolute;left:54px;top:1330px;width:300px;font-size:24px;font-weight:900;line-height:1.25}
.thanks-box{position:absolute;left:345px;top:1305px;width:669px;height:177px;border:2px solid var(--teal)}
.thanks-box .cap{position:absolute;left:50%;transform:translateX(-50%);background:var(--paper);padding:0 14px;color:var(--teal);font-weight:900;font-size:22px;white-space:nowrap}
.thanks-box .cap--top{top:-15px;letter-spacing:1px}
.thanks-box .cap--bottom{bottom:-15px;font-size:21px}
.badges{position:absolute;left:22px;right:22px;top:30px;display:flex;gap:10px}
.badge{flex:1;height:115px;border:1px solid #ccc}
.badge--1{background:#f3eee9}
.badge--2{background:var(--crimson)}
.badge--3{background:#0f2147}
.badge--4{background:#f4f4f4}
</style>
</head>
<body>

<section class="sheet sheet--front">
  <svg class="front-art" viewBox="0 0 1070 1515" aria-hidden="true">
    <path d="M0,0 H1070 V540 C900,600 760,700 560,700 C360,700 160,640 0,720 Z" fill="#e8612c"/>
    <path d="M0,780 C140,700 420,700 580,770 C660,920 620,1150 500,1260 C320,1340 90,1300 0,1260 Z" fill="#1f55a6"/>
    <path d="M470,730 C640,620 950,600 1070,650 V1290 C900,1330 650,1300 530,1210 C430,1060 400,860 470,730 Z" fill="#e8612c" opacity=".92"/>
    <path d="M500,760 C580,760 620,900 590,1060 C570,1160 540,1220 520,1215 C440,1080 420,880 500,760 Z" fill="#3a2b2a" opacity=".85"/>
    <path d="M0,1330 C200,1210 500,1200 700,1235 C850,1260 980,1290 1070,1255 V1515 H0 Z" fill="#a9c3a8"/>
    <g fill="none" stroke-width="3">
      <path d="M880,0 C960,120 1040,260 1070,330" stroke="#0f4a3a"/>
      <path d="M0,220 C300,160 620,300 820,600" stroke="#0f4a3a"/>
      <path d="M60,0 C200,300 500,520 780,580 C900,600 1000,560 1070,520" stroke="#16868a"/>
      <path d="M0,600 C250,560 520,610 700,700" stroke="#ffffff" opacity=".6"/>
      <path d="M960,0 C990,200 1000,400 980,560" stroke="#16868a"/>
    </g>
  </svg>

  <h1 class="title">Harriet Voss Consortium</h1>
  <p class="subtitle">Paediatric Lower Limb Surgery Agenda Forming Collective</p>
  <div class="brand-box"><span class="dot"></span><span class="name">Harriet Voss Consortium</span></div>
  <div class="divider"></div>

  <p class="intro intro--left">Surgery is often carried out amongst children with conditions that their legs, but in many conditions, it is not known which treatment works best. We need high-quality research to test which treatments are better for children.</p>
  <p class="intro intro--right">We reached out to everybody involved with children who have orthopaedic problems affecting their legs (from hip to toes), including children, parents, carers, charity workers, and all the professional groups. We asked all for their views on identifying the most important unanswered questions.</p>

  <div class="stage stage--ask">
    <div class="label">Stage 1</div>
    <div class="word">ASK</div>
    <p>Our UK-wide survey of patients, carers, physiotherapists, nurses and surgeons asked</p>
    <p class="quote">“What is the most important unanswered question amongst children undergoing planned surgery for conditions affecting their legs”</p>
  </div>

  <div class="stage stage--analyse">
    <div class="label">Stage 2</div>
    <div class="word">ANALYSE</div>
    <p>We reviewed <strong>1023 questions from 388 people</strong>, and sorted these into 76 unique themed questions.</p>
  </div>

  <div class="stage stage--prioritise">
    <div class="label">Stage 3</div>
    <div class="word">PRIORITISE</div>
  </div>
  <p class="stage3-text">From those we asked patients, carers, physiotherapists, nurses and surgeons to tell us <strong>“What are your top-10 most important questions”</strong>. This created a shortlist that were prioritized at a final workshop</p>
</section>

<section class="sheet sheet--back">
  <h2 class="heading"><span class="lead">Our top-10</span><span class="band">RESEARCH PRIORITIES:</span></h2>
  <ol class="priorities">
    <li class="priority priority--l c-orange"><span class="num">1</span><span class="q">What are the best ways to measure the outcome following lower limb orthopaedic surgery in children?</span></li>
    <li class="priority priority--r c-teal"><span class="q">Following orthopaedic surgery to the lower limbs, what should children’s rehabilitation include, how long is it expected to last and how does it affect the result of treatment?</span><span class="num">2</span></li>
    <li class="priority priority--l c-crimson"><span class="num">3</span><span class="q">What is the short-term and long-term clinical and cost effectiveness of orthopaedic lower limb surgery (including best timing and technique) for children with Cerebral Palsy who can walk?</span></li>
    <li class="priority priority--r c-sage"><span class="q">What are the short term and long term outcomes of surgery compared to non-surgical care in the treatment of Perthes disease of the hip?</span><span class="num">4</span></li>
    <li class="priority priority--l c-blue"><span class="num">5</span><span class="q">What is the clinical and cost effectiveness of pre-operative rehabilitation in children presenting with lower limb orthopaedic conditions?</span></li>
    <li class="priority priority--r c-lime"><span class="q">What is the short-term and long-term clinical and cost effectiveness of Selective Dorsal Rhizotomy (SDR) in children with Cerebral Palsy who can walk?</span><span class="num">6</span></li>
    <li class="priority priority--l c-orange"><span class="num">7</span><span class="q">Can surveillance and non-surgical treatment (e.g. physiotherapy, botulinum toxin injections, functional electrical stimulation, orthotics, casting) prevent the development of deformity requiring surgery in children with Cerebral Palsy?</span></li>
    <li class="priority priority--r c-teal"><span class="q">What is the best method of screening for Developmental Dysplasia of the Hip (DDH) in terms of clinical and cost effectiveness?</span><span class="num">8</span></li>
    <li class="priority priority--l c-sage"><span class="num">9</span><span class="q">What are the best strategies to optimise communication of information between patients/carers and clinicians in order to enable shared decision-making?</span></li>
    <li class="priority priority--r c-lime"><span class="q">What is the best management for hip displacement in children with Cerebral Palsy?</span><span class="num">10</span></li>
  </ol>

  <p class="thanks-note">Many thanks to all those people who helped us take this work off the ground and helped us finish it!</p>
  <div class="thanks-box">
    <span class="cap cap--top">SPECIAL THANKS TO</span>
    <div class="badges">
      <div class="badge badge--1" role="img" aria-label="Partner badge"></div>
      <div class="badge badge--2" role="img" aria-label="Partner badge"></div>
      <div class="badge badge--3" role="img" aria-label="Partner badge"></div>
      <div class="badge badge--4" role="img" aria-label="Partner badge"></div>
    </div>
    <span class="cap cap--bottom">who always look for fair play in research!</span>
  </div>
</section>

</body>
</html>
```